依頼詳細
恥を忍んで書きます。主にシステム側を得意とする自分が、デザインも含めた案件を引き受けてしまい、トップページのデザイン案として以下の2つを作成したところ、クオリティ不足を言い渡されてしまいました。ごもっともだと自覚しています。
http://pelmo.jp/up/tarucs-green.jpg
http://pelmo.jp/up/tarucs-blue.jpg

上記のつたないデザイン案で問題ないのはページ内の「要素」だけですので、デザインのブラッシュアップ、または抜本的なリフレッシュをお願いします。ひとまずトップページ画像だけで大丈夫です。

なお、過去にWordPressテンプレートサイトのデザインに企業名を充てただけの以下のデザインは気に入っていただいています。このテイストをまるごと使ってもかまいません。
http://templates.vorlinquest.com/template_number/live_demo.asp?TemplateID=41938
http://pelmo.jp/up/tarucs-template.jpg

できれば9/2(月)いっぱいくらいで先方に提示したいと考えていて、無謀なスケジュールなので、手を上げていただける方の労力ができるだけ無駄にならないようにしたいです。
サイトURL
http://www.tarucs.co.jp/
ページ数
1ページ
希望イメージ
シンプル 複雑
単色 カラフル
暗い 明るい
日常 高級
遊び心 厳粛
未来的 伝統的
女性的 男性的
希望する色
緑ないし青ベースで、黄と赤をアクセントにとの先方の希望です。
納品ファイル
• 高解像度JPG (.jpg)
• イラストレーター形式 (.ai)
補足説明
ここにメアドを書いていいのかわかりませんが、詳細はお気軽にお問い合わせください。
ご質問など承りますし、素材などもお送りいたします。
mあっとpelmo.jp
追記補足です。
トップページのメイン画像は、
よくある複数パターンの切り替え式(時間経過かクリック)の予定です。
とりあえず今回のご提案では「すばらしい自然を未来の子供たちに…」の
メッセージのもので大丈夫ですが、切り替え式となることをご考慮ください。
これから提案をご予定の方々には申し訳ありません。

過去にクライアントに気に入っていただいたWordPressテンプレートのイメージをうまく活かして、きれいにまとめていただいたdorusan72様に決めさせていただきました。テンプレートのイメージに沿わせるべきか、オリジナリティを出すほうがいいかは、わたしも判断に迷うところでしたが、最終的には先方に選んでいただきました。
青バージョンとして色のイメージを参考にさせていただいたmepolt様、そしてWordPress構築を意識してデザインしていただいたranpu様を次点として選ばせていただきました。

短期のスケジュールだった上に途中でほぼ即決の方向で調整させていただきまして、ランサーの皆様にはご迷惑おかけしてしまいました。
初めてのハルモワークスの利用でしたが、こんなに短期間でクオリティの高いご提案がいただけて大変感激しています。もちろん、次に利用させていただくときはこんなスケジュールにならないようにしたいと思います。
ご提案に至らなかった皆様も含めまして、ありがとうございました。

```html
<!DOCTYPE html>
<html lang="ja">
<head>
<meta charset="utf-8">
<title>株式会社タルクス | 自然エネルギー事業</title>
<link href="https://fonts.googleapis.com/css2?family=Noto+Sans+JP:wght@400;700&family=Noto+Serif+JP:wght@700&display=swap" rel="stylesheet">
<style>
:root{
  --navy:#0f2d63;
  --blue:#1f5fae;
  --sky:#5fa3dc;
  --pale:#e4ecf2;
  --line:#c9d6e0;
  --green:#3f8f2e;
  --lime:#9fcf4a;
  --red:#d7322a;
  --yellow:#f2c316;
  --text:#333;
  --white:#fff;
}
*{box-sizing:border-box;margin:0;padding:0}
html,body{width:800px;height:1200px;overflow:hidden}
body{background:linear-gradient(#cfdbe5,#e8eef3 30%,#e8eef3);font-family:"Noto Sans JP",sans-serif;color:var(--text);font-size:9px;line-height:1.5}
.page{width:688px;margin:0 auto;position:relative;height:1200px}

.site-header{height:75px;background:linear-gradient(90deg,var(--navy),var(--blue) 60%,var(--navy));display:flex;align-items:center;padding:0 18px;gap:12px}
.logo{display:flex;align-items:center;gap:8px;color:var(--white);font-weight:700;font-size:28px;letter-spacing:3px}
.logo-mark{width:10px;height:10px;background:var(--yellow)}
.tagline{color:#cfe0f3;font-size:8px;line-height:1.4}
.header-visual{width:130px;height:60px;margin-left:auto;background:linear-gradient(135deg,#2c5d9c,#8fb8e0);border-radius:4px}
.contact{color:var(--white);text-align:right;margin-left:22px}
.contact small{display:block;font-size:8px;color:#cfe0f3}
.contact .tel{display:flex;align-items:center;gap:4px;font-size:17px;font-weight:700}

.hero{height:298px;display:flex;background:linear-gradient(#7fb7e6,#d6ebf8 70%,#8fc36a)}
.hero-photo{width:330px;height:100%;background:linear-gradient(160deg,#6ea84a,#b8d98a 45%,#8ab7de)}
.hero-copy{flex:1;position:relative;padding:40px 18px 0 20px}
.hero-turbines{position:absolute;right:0;bottom:0;width:200px;height:150px;background:linear-gradient(#bfdcf1,#e6f1f8)}
.hero-lead{font-size:11px;color:var(--navy);position:relative}
.hero-title{font-family:"Noto Serif JP",serif;font-size:21px;line-height:1.45;color:var(--navy);margin:6px 0 18px;position:relative}
.hero-sub{font-size:10px;color:var(--navy);position:relative}
.hero-sub strong{font-size:13px;display:block}

.global-nav{height:27px;background:linear-gradient(#fdfdfd,#dfe6ec);display:flex;border-bottom:2px solid var(--blue)}
.global-nav a{flex:1;text-align:center;line-height:27px;color:var(--blue);font-size:10px;text-decoration:none;border-right:1px solid var(--line)}
.global-nav a:first-child{background:var(--blue);color:var(--white)}

.content{display:flex;gap:14px;padding:14px 0 0;background:var(--white);height:590px}
.sidebar{width:197px}
.banner{height:48px;margin-bottom:5px;border:1px solid #b7d59b;background:linear-gradient(90deg,#f4faee,#dcefc8);display:flex;align-items:center;padding:0 6px;gap:6px;color:var(--green);font-size:9px;font-weight:700;line-height:1.35}
.banner-photo{width:64px;height:38px;flex:none;background:linear-gradient(135deg,#7fae4f,#c6e09a)}
.banner:nth-child(2) .banner-photo{background:linear-gradient(135deg,#4d87c7,#a9cbe9)}
.banner:nth-child(4) .banner-photo{background:linear-gradient(135deg,#e0b43a,#f4e3a0)}
.side-box{border:1px solid var(--line);margin-top:10px;padding:6px}
.side-title{background:var(--blue);color:var(--white);font-size:9px;padding:2px 6px;margin-bottom:6px}
.sns{height:40px;border:1px solid var(--line);display:flex;align-items:center;padding:0 8px;color:var(--text);font-weight:400;font-size:10px}
.badge{height:30px;margin-top:6px;background:linear-gradient(90deg,#e9edf0,#d3dbe1);border:1px solid var(--line)}
.badge.warm{background:linear-gradient(90deg,#f7e9c4,#f2d27a)}

.main{flex:1}
.intro{background:linear-gradient(#f5f9fc,#e9f1f7);border:1px solid var(--line);padding:12px 14px;height:108px}
.intro h2{font-size:11px;color:var(--green);margin-bottom:4px}
.intro p{font-size:9px;color:#555}
.sec-title{margin:12px 0 8px;border-bottom:2px solid var(--blue);height:20px}
.sec-title span{display:inline-block;background:var(--blue);color:var(--white);font-size:9px;padding:2px 14px;line-height:18px}
.pickup{display:flex;gap:8px}
.card{flex:1}
.card-photo{height:70px;border:1px solid var(--line)}
.card p{font-size:8px;margin-top:3px;color:#444;line-height:1.4}
.news{list-style:none}
.news li{display:flex;gap:12px;border-bottom:1px dotted var(--line);line-height:21px;font-size:8.5px}
.news time{color:#777;flex:none}
.news a{color:var(--blue);text-decoration:none}

.to-top{text-align:right;height:24px;padding:6px 8px 0 0;font-size:8px;color:var(--blue);background:var(--white)}

.site-footer{position:absolute;left:0;right:0;top:1030px;height:170px;background:linear-gradient(var(--blue),var(--navy));color:var(--white);padding:14px 18px 0}
.footer-inner{display:flex;gap:24px}
.footer-company{width:170px}
.footer-company .logo{font-size:22px}
.footer-company p{font-size:8px;color:#d5e3f2;margin-top:6px}
.footer-links{flex:1;display:flex;gap:18px}
.footer-links ul{list-style:none;flex:1}
.footer-links li{font-size:8px;color:#dfeaf6;line-height:1.9}
.footer-links li:first-child{color:var(--yellow);font-weight:700}
.copyright{position:absolute;left:0;right:0;bottom:0;height:22px;background:#0a2149;font-size:8px;color:#b9cbe0;line-height:22px;padding-left:18px}
</style>
</head>
<body>
<div class="page">
  <header class="site-header">
    <div class="logo"><span class="logo-mark"></span>TARUCS</div>
    <p class="tagline">株式会社タルクス<br>自然エネルギー事業を支援します。</p>
    <div class="header-visual" role="img" aria-label="ソーラーパネルの写真"></div>
    <div class="contact">
      <small>お問い合わせ・ご相談窓口</small>
      <span class="tel"><svg width="14" height="14" viewBox="0 0 24 24"><path fill="#fff" d="M6.6 10.8a15 15 0 0 0 6.6 6.6l2.2-2.2a1 1 0 0 1 1-.25 11.4 11.4 0 0 0 3.6.57 1 1 0 0 1 1 1V20a1 1 0 0 1-1 1A17 17 0 0 1 3 4a1 1 0 0 1 1-1h3.5a1 1 0 0 1 1 1c0 1.25.2 2.45.57 3.57a1 1 0 0 1-.25 1z"/></svg>072-000-4518</span>
    </div>
  </header>

  <section class="hero">
    <div class="hero-photo" role="img" aria-label="木に登って遊ぶ子供たちの写真"></div>
    <div class="hero-copy">
      <div class="hero-turbines" role="img" aria-label="青空に並ぶ風力発電の風車"></div>
      <p class="hero-lead">すばらしい自然を未来の子供たちに残すために〜</p>
      <h1 class="hero-title">新しいエネルギー社会を<br>私たちと一緒に創りませんか？</h1>
      <p class="hero-sub">未来へつなぐ自然エネルギー商事を提案する会社<strong>株式会社タルクス</strong></p>
    </div>
  </section>

  <nav class="global-nav">
    <a href="#">トップページ</a><a href="#">会社概要</a><a href="#">コンサルティング事業</a><a href="#">新エネルギー事業</a><a href="#">お問い合わせ</a>
  </nav>

  <div class="content">
    <aside class="sidebar">
      <div class="banner"><span class="banner-photo" role="img" aria-label="太陽光発電の写真"></span>自然エネルギーを<br>暮らしの中に</div>
      <div class="banner"><span class="banner-photo" role="img" aria-label="風力発電の写真"></span>コンサルティング<br>事業のご案内</div>
      <div class="banner"><span class="banner-photo" role="img" aria-label="緑の風景の写真"></span>新エネルギー<br>事業のご案内</div>
      <div class="banner"><span class="banner-photo" role="img" aria-label="設備の写真"></span>施工実績の<br>ご紹介</div>
      <div class="side-box">
        <p class="side-title">最新情報はこちら</p>
        <div class="sns">Tomobook</div>
        <div class="badge"></div>
        <div class="badge"></div>
        <div class="badge warm"></div>
      </div>
    </aside>

    <main class="main">
      <div class="intro">
        <h2>自然エネルギーの推進、今日は未来の子供達への橋渡しの日です</h2>
        <p>株式会社タルクスは、自然エネルギーの普及を通じて、地域の皆様と共に持続可能な社会づくりを進めています。太陽光・風力などの導入に関するご相談から設計、施工、保守まで一貫してお手伝いいたします。お気軽にお問い合わせください。</p>
      </div>

      <h3 class="sec-title"><span>ピックアップ</span></h3>
      <div class="pickup">
        <div class="card"><div class="card-photo" role="img" aria-label="屋根の太陽光パネル" style="background:linear-gradient(135deg,#2d5f9a,#9cc2e6)"></div><p>太陽光発電の導入事例を紹介します</p></div>
        <div class="card"><div class="card-photo" role="img" aria-label="広い敷地の発電設備" style="background:linear-gradient(135deg,#5c8fc4,#d0e3f2)"></div><p>大規模発電所の計画と運用について</p></div>
        <div class="card"><div class="card-photo" role="img" aria-label="小型風車" style="background:linear-gradient(135deg,#8a9aa8,#e1e7ec)"></div><p>小型風力発電の新しい取り組み</p></div>
        <div class="card"><div class="card-photo" role="img" aria-label="風力発電の風車" style="background:linear-gradient(135deg,#6fa8da,#e4f0f9)"></div><p>地域と共に進める風力発電事業</p></div>
      </div>

      <h3 class="sec-title"><span>新着情報</span></h3>
      <ul class="news">
        <li><time>2013.08.30</time><a href="#">自然エネルギー推進セミナーを開催しました。</a></li>
        <li><time>2013.08.22</time><a href="#">太陽光発電システムの施工実績を更新しました。</a></li>
        <li><time>2013.08.10</time><a href="#">夏季休業のお知らせ</a></li>
        <li><time>2013.07.28</time><a href="#">新エネルギー事業のご案内ページを公開しました。</a></li>
        <li><time>2013.07.15</time><a href="#">ホームページをリニューアルしました。</a></li>
        <li><time>2013.07.01</time><a href="#">会社概要を更新しました。</a></li>
      </ul>
    </main>
  </div>
  <p class="to-top">▲ ページトップへ</p>

  <footer class="site-footer">
    <div class="footer-inner">
      <div class="footer-company">
        <div class="logo"><span class="logo-mark"></span>TARUCS</div>
        <p>株式会社タルクス<br>〒000-0000<br>大阪府○○市△△町1-2-3<br>TEL 072-000-4518</p>
      </div>
      <div class="footer-links">
        <ul><li>トップページ</li><li>お知らせ</li><li>施工実績</li></ul>
        <ul><li>会社概要</li><li>代表挨拶</li><li>沿革</li><li>アクセス</li></ul>
        <ul><li>コンサルティング事業</li><li>導入相談</li><li>設計</li></ul>
        <ul><li>新エネルギー事業</li><li>太陽光</li><li>風力</li><li>お問い合わせ</li></ul>
      </div>
    </div>
    <p class="copyright">Copyright © TARUCS Co., Ltd. All Rights Reserved.</p>
  </footer>
</div>
</body>
</html>
```